Design the Keystone HR business card for my new business

I've just had a logo designed (attached) for my new business doing HR consulting. I'm a one person operation at this stage, my aim is to provide support and help to small to medium sized businesses with their people objectives or issues.

I'm not really into anything overly flashy, I'm not a PR or marketing agency. I'd like my card to look modern, professional and not gimmicky.

I'm thinking black front (to go with logo), double sided with details on the back, maybe in a different colour?

Logo attached in several different formats.

Front of the card to have logo and added text: People and Development Solutions

Back of the card to also feature logo in some way and say:
Megan Turlow
PO Box (TBA)
Marnoo Flats QLD 4381
0427 318 562
megan@keystonehr-example.com.au
www.keystonehr-example.com.au

Target Market(s)

Small to medium businesses / business owners.

Industry/Entity Type

Marketing

Requirements
Must have
• Double sided business card.
Should not have
• Anything overly gimmicky.

```html
<!DOCTYPE html>
<html lang="en">
<head>
<meta charset="utf-8">
<title>Keystone HR – Business Card</title>
<link rel="stylesheet" href="https://fonts.googleapis.com/css2?family=Dosis:wght@400;500&display=swap">
<style>
  :root {
    --page-bg: #ffffff;
    --card-bg: #000000;
    --ink-light: #ffffff;
    --band-grey: #7b7b7b;
    --glow-purple: #5a2a78;
    --accent-purple: #7b3fa6;
  }
  html, body {
    margin: 0;
    padding: 0;
    width: 1200px;
    height: 900px;
    overflow: hidden;
    background: var(--page-bg);
  }
  .canvas {
    position: relative;
    width: 1200px;
    height: 900px;
    font-family: "Dosis", sans-serif;
  }
  .card {
    position: absolute;
    left: 310px;
    width: 576px;
    height: 320px;
    background: var(--card-bg);
    overflow: hidden;
  }
  .card--back { top: 60px; height: 318px; }
  .card--front { top: 484px; }

  .back-glow {
    position: absolute;
    left: 0;
    top: 0;
    width: 260px;
    height: 240px;
    background: radial-gradient(ellipse at 45% 35%, rgba(90, 42, 120, 0.45) 0%, rgba(90, 42, 120, 0.15) 40%, rgba(0, 0, 0, 0) 70%);
  }
  .contact {
    position: absolute;
    left: 0;
    right: 0;
    top: 44px;
    margin: 0;
    padding: 0;
    list-style: none;
    text-align: center;
    color: var(--ink-light);
    font-size: 21px;
    line-height: 33px;
    font-weight: 400;
    letter-spacing: 0.3px;
  }
  .contact__item--name { padding-left: 40px; }

  .brand {
    position: absolute;
    left: 46px;
    top: 82px;
    display: flex;
    align-items: center;
    gap: 22px;
  }
  .brand__dot {
    width: 124px;
    height: 124px;
    border-radius: 50%;
    background: var(--accent-purple);
  }
  .brand__name {
    color: var(--ink-light);
    font-size: 66px;
    font-weight: 400;
    line-height: 1;
    white-space: nowrap;
  }
  .tagline-band {
    position: absolute;
    left: 0;
    right: 0;
    top: 266px;
    height: 30px;
    background: var(--band-grey);
    color: var(--ink-light);
    font-size: 17px;
    line-height: 30px;
    padding-left: 14px;
    letter-spacing: 0.2px;
  }
</style>
</head>
<body>
<main class="canvas">
  <section class="card card--back" aria-label="Card back">
    <div class="back-glow" role="img" aria-label="Faint purple brand glow"></div>
    <ul class="contact">
      <li class="contact__item contact__item--name">Megan Turlow</li>
      <li class="contact__item">PO Box (TBA)</li>
      <li class="contact__item">Marnoo Flats QLD 4381</li>
      <li class="contact__item">0427 318 562</li>
      <li class="contact__item">megan@keystonehr-example.com.au</li>
      <li class="contact__item">www.keystonehr-example.com.au</li>
    </ul>
  </section>

  <section class="card card--front" aria-label="Card front">
    <div class="brand">
      <span class="brand__dot" aria-hidden="true"></span>
      <span class="brand__name">Keystone HR</span>
    </div>
    <div class="tagline-band">People and Development Solutions</div>
  </section>
</main>
</body>
</html>
```